KESTRIDGE PAINTING

We are a painting company. We paint residential, commercial and strata jobs. I need the website to be very sharp, neat and elegant. I've attached our logo. the Logo needs to be embossed as a gold color and the background like a Matt black. I need these tabs:

• HOME • ABOUT US • SERVICES • TESTIMONIALS • SHOWCASE • CONTACT US

Be creative and innovative in your style.
take this as an example to just get the gist of what I'm expecting. If you can better it then the job is yours!

http://marlowvinepainting.com.au/contact.html

I look forward to seeing your artwork :)

#These are the links to my logo in PSD format.

https://www.filevaultic.com/s/qwpzrtk4n7hd2aa/Kestridge%20Painting%20Luxury%20Gold.rar

https://www.filevaultic.com/sh/rkvbnxq2p5yhw7/QaLm8-vbSx

• Making the Logo embossed like the artworks i have attached is definitely a necessity.

Can you let me know if this is possible to apply to the website.

thank you

```html
<!DOCTYPE html>
<html lang="en">
<head>
<meta charset="utf-8">
<title>Kestridge Painting</title>
<link rel="stylesheet" href="https://fonts.googleapis.com/css2?family=PT+Sans:ital,wght@0,400;0,700;1,400&family=PT+Sans+Narrow:wght@400;700&display=swap">
<style>
:root{
  --bg-deep:#0b0806;
  --bg-warm:#5a3a1c;
  --gold:#c9a43a;
  --gold-light:#e0bf55;
  --gold-dark:#9c7a22;
  --tab-top:#5d5e61;
  --tab-bottom:#3b3c3f;
  --text:#f2ece2;
  --muted:#9a928a;
  --panel:#141210;
  --footer:#2a2a2b;
  --line:#6e645a;
}
*{margin:0;padding:0;box-sizing:border-box}
html,body{width:995px;height:1200px;overflow:hidden}
body{
  position:relative;
  font-family:"PT Sans",Arial,sans-serif;
  color:var(--text);
  background:
    radial-gradient(ellipse 420px 300px at 500px 40px,rgba(140,95,45,.55),transparent 70%),
    radial-gradient(ellipse 700px 520px at 560px 420px,rgba(110,72,34,.55),transparent 75%),
    radial-gradient(ellipse 900px 700px at 500px 300px,var(--bg-warm),var(--bg-deep) 80%);
}
.abs{position:absolute}
.heading{font-family:"PT Sans Narrow","PT Sans",sans-serif;font-weight:700;color:#fff;text-transform:uppercase}

/* header */
.brand-mark{left:444px;top:8px;width:84px;height:84px;border:3px solid var(--gold);border-radius:50%}
.brand-name{left:300px;width:372px;top:101px;text-align:center;font-weight:700;font-size:17px;color:#fff;letter-spacing:.2px}
.brand-tagline{left:300px;width:372px;top:119px;text-align:center;font-size:7.5px;color:#e8e2d8}
.call{left:660px;width:186px;top:102px;text-align:right;font-size:12px;color:#fff}

/* nav */
.nav{left:150px;top:142px;width:699px;height:41px;display:flex;list-style:none}
.nav li{flex:1;display:flex;align-items:center;justify-content:center;font-size:10px;font-weight:700;color:#fff;
  background:linear-gradient(var(--tab-top),var(--tab-bottom));border-right:1px solid #27282a;border-bottom:2px solid #7a7b7e}
.nav li:last-child{border-right:none}
.nav li.active{background:linear-gradient(var(--gold-light),var(--gold-dark));border-bottom-color:#e8c968}

/* hero */
.hero{left:149px;top:204px;width:697px;height:299px;background:#fff;padding:6px;box-shadow:0 6px 18px rgba(0,0,0,.5)}
.hero-photo{width:100%;height:100%;
  background:linear-gradient(180deg,#fbfbfb 0%,#e9e6e2 20%,#4a4d55 32%,#b59a78 55%,#8a6c50 72%,#3f6a2c 88%,#5a8a3a 100%)}
.slide-arrows{left:789px;top:465px;display:flex;gap:1px}
.slide-arrows span{width:22px;height:25px;background:rgba(40,40,40,.55);display:flex;align-items:center;justify-content:center}

/* welcome */
.welcome-title{left:150px;width:696px;top:534px;text-align:center;font-size:21px;font-family:"PT Sans",sans-serif;font-weight:400}
.welcome-text{left:160px;width:676px;top:570px;text-align:center;font-size:8.4px;line-height:14.4px;color:#fff}

/* section heads */
.section-title{font-size:14.5px;font-family:"PT Sans",sans-serif;font-weight:400;color:#fff}
.mini-arrows{display:flex;gap:3px}
.mini-arrows span{width:11px;height:12px;background:#4a4644;display:flex;align-items:center;justify-content:center}
.rule{left:150px;top:659px;width:696px;height:1px;background:var(--line)}

/* service cards */
.card{width:161px}
.card-photo{width:161px;height:97px;background:#fff;padding:4px}
.card-photo div{width:100%;height:100%}
.card h3{margin-top:13px;margin-left:3px;font-size:11px;font-family:"PT Sans",sans-serif;font-weight:700;color:#fff}
.card p{margin:5px 0 0 4px;font-size:7px;line-height:14.3px;color:var(--muted)}
.btn{display:inline-flex;align-items:center;justify-content:center;width:75px;height:19px;font-size:8px;color:#fff;
  background:linear-gradient(var(--gold-light),var(--gold-dark))}
.card .btn{margin:9px 0 0 3px}

/* about */
.about-photo{left:150px;top:951px;width:161px;height:91px;background:#fff;padding:4px}
.about-photo div{width:100%;height:100%;background:linear-gradient(100deg,#a6741e 0%,#e0c23e 30%,#e8cd4a 70%,#d9b73a 100%)}
.about-text{font-size:7px;line-height:14.4px;color:var(--muted)}

/* testimonial */
.quote-box{left:584px;top:947px;width:262px;height:98px;background:var(--panel);border:1px solid #2b2723}
.quote-box p{position:absolute;left:36px;top:15px;width:205px;font-size:7px;line-height:14.3px;color:var(--muted)}
.quote-mark{font-family:Georgia,serif;font-size:20px;color:#8a837c;position:absolute}
.avatar{left:585px;top:1064px;width:46px;height:40px;border:2px solid #4a4541;
  background:linear-gradient(160deg,#3d4a33,#7a6a55 55%,#d9d0c3)}
.author{left:645px;top:1066px;font-size:7.5px;color:var(--gold)}
.posted{left:645px;top:1081px;font-size:7px;font-style:italic;color:var(--muted)}

/* footer */
.footer{left:149px;top:1142px;width:697px;height:58px;background:var(--footer)}
.footer-links{position:absolute;left:24px;top:16px;display:flex;font-size:6.4px;color:#e8e4de;list-style:none}
.footer-links li+li::before{content:"|";margin:0 14px 0 14px;color:#cfcac3}
.copyright{position:absolute;left:24px;top:34px;font-size:6.4px;color:#e8e4de}
.follow{position:absolute;left:533px;top:24px;font-size:6.4px;color:#e8e4de}
.social{position:absolute;top:17px;width:23px;height:23px;border-radius:50%;background:#5b5c5e}
</style>
</head>
<body>

<header>
  <div class="abs brand-mark"></div>
  <div class="abs brand-name">KESTRIDGE PAINTING</div>
  <div class="abs brand-tagline">Painting Australia Everyday!</div>
  <div class="abs call">CALL US : ( 0200 ) 555 014</div>
  <ul class="abs nav">
    <li class="active">HOME</li>
    <li>ABOUT US</li>
    <li>SERVICES</li>
    <li>TESTIMONIALS</li>
    <li>SHOWCASE</li>
    <li>CONTACT US</li>
  </ul>
</header>

<section class="abs hero">
  <div class="hero-photo" role="img" aria-label="Photograph of a large two-storey rendered house with a dark shingle roof, white trim and front lawn"></div>
</section>
<div class="abs slide-arrows">
  <span><svg width="8" height="12" viewBox="0 0 8 12"><path d="M6 1 1 6l5 5" fill="none" stroke="#fff" stroke-width="1.6"/></svg></span>
  <span><svg width="8" height="12" viewBox="0 0 8 12"><path d="M2 1l5 5-5 5" fill="none" stroke="#fff" stroke-width="1.6"/></svg></span>
</div>

<h1 class="abs welcome-title">WELCOME TO KESTRIDGE PAINTING</h1>
<p class="abs welcome-text">It is a long established fact that a reader will be distracted by the readable content of a page when looking at its layout. The point of using Lorem Ipsum is that it has a more-or-less normal distribution of letters, as opposed to using 'Content here, content here', making it look like readable English. Many desktop publishing packages and web page editors now use Lorem Ipsum as their default model text, and a search for 'lorem ipsum' will uncover many web sites still in their infancy.</p>

<h2 class="abs section-title" style="left:150px;top:630px">SERVICES</h2>
<div class="abs mini-arrows" style="left:818px;top:636px">
  <span><svg width="5" height="7" viewBox="0 0 5 7"><path d="M4 .5 1 3.5l3 3" fill="none" stroke="#ccc"/></svg></span>
  <span><svg width="5" height="7" viewBox="0 0 5 7"><path d="M1 .5l3 3-3 3" fill="none" stroke="#ccc"/></svg></span>
</div>
<div class="abs rule"></div>

<article class="abs card" style="left:150px;top:678px">
  <div class="card-photo"><div role="img" aria-label="Photograph of painters on ladders painting a blue weatherboard wall" style="background:linear-gradient(120deg,#6f8ea8,#4f6e88 60%,#c9c3b8)"></div></div>
  <h3>COMMERCIAL PAINTING</h3>
  <p>It is a long established fact that a reader will be distracted by the readable content of a page when looking at its layout...</p>
  <span class="btn">READ MORE</span>
</article>
<article class="abs card" style="left:327px;top:678px">
  <div class="card-photo"><div role="img" aria-label="Photograph of a fanned-out paint colour swatch deck" style="background:linear-gradient(110deg,#2f8a7a,#c02a3a 35%,#e87a6a 55%,#f0c8a0 80%,#f3e0c6)"></div></div>
  <h3>COLOR CONSULTING</h3>
  <p>It is a long established fact that a reader will be distracted by the readable content of a page when looking at its layout...</p>
  <span class="btn">READ MORE</span>
</article>
<article class="abs card" style="left:505px;top:678px">
  <div class="card-photo"><div role="img" aria-label="Photograph of two workers painting a dark green timber fence" style="background:linear-gradient(100deg,#2f4a40,#3d6a5a 50%,#24392f)"></div></div>
  <h3>FENCE PAINTING</h3>
  <p>It is a long established fact that a reader will be distracted by the readable content of a page when looking at its layout...</p>
  <span class="btn">READ MORE</span>
</article>
<article class="abs card" style="left:683px;top:678px">
  <div class="card-photo"><div role="img" aria-label="Photograph of a modern house with grey-blue timber cladding" style="background:linear-gradient(180deg,#7aa6d6,#a9c4de 35%,#7d8c96 60%,#4f5c66)"></div></div>
  <h3>EXTERIOR TIMBER MAINTENANCE</h3>
  <p>It is a long established fact that a reader will be distracted by the readable content of a page when looking at its layout...</p>
  <span class="btn">READ MORE</span>
</article>

<h2 class="abs section-title" style="left:150px;top:916px">ABOUT KESTRIDGE PAINTING</h2>
<div class="abs about-photo"><div role="img" aria-label="Photograph of a painter on a ladder rolling yellow paint onto a wall"></div></div>
<p class="abs about-text" style="left:325px;top:949px;width:230px">It is a long established fact that a reader will be distracted by the readable content of a page when looking at its layout. The point of using Lorem Ipsum is that it has a more-or-less normal distribution of letters, as opposed to using 'Content here, content here', making it look like readable English. Many desktop publishing packages and web page editors now use Lorem Ipsum as their default model text, and a search for 'lorem ipsum' will uncover many web sites still in their infancy.</p>
<p class="abs about-text" style="left:150px;top:1055px;width:410px">It is a long established fact that a reader will be distracted by the readable content of a page when looking at its layout. The point of using Lorem Ipsum is that it has a more-or-less normal distribution...</p>
<span class="abs btn" style="left:150px;top:1098px">READ MORE</span>

<h2 class="abs section-title" style="left:583px;top:916px">TESTIMONIALS</h2>
<div class="abs mini-arrows" style="left:818px;top:920px">
  <span><svg width="5" height="7" viewBox="0 0 5 7"><path d="M4 .5 1 3.5l3 3" fill="none" stroke="#ccc"/></svg></span>
  <span><svg width="5" height="7" viewBox="0 0 5 7"><path d="M1 .5l3 3-3 3" fill="none" stroke="#ccc"/></svg></span>
</div>
<div class="abs quote-box">
  <span class="quote-mark" style="left:14px;top:6px">&ldquo;</span>
  <p>It is a long established fact that a reader will be distracted by the readable content of a page when looking at its layout. The point of using Lorem Ipsum is that it has a more-or-less normal distribution of letters...</p>
  <span class="quote-mark" style="left:236px;top:68px">&rdquo;</span>
</div>
<svg class="abs" style="left:740px;top:1044px" width="56" height="30" viewBox="0 0 56 30"><path d="M0 0h56L4 28z" fill="#141210"/></svg>
<div class="abs avatar" role="img" aria-label="Portrait photo of the client"></div>
<div class="abs author">MARCUS ELLERY</div>
<div class="abs posted">Posted on 20 Aug 2013</div>

<footer class="abs footer">
  <ul class="footer-links">
    <li>HOME</li><li>ABOUT US</li><li>SERVICES</li><li>TESTIMONIALS</li><li>SHOWCASE</li><li>CONTACT US</li>
  </ul>
  <div class="copyright">COPYRIGHT © 2013. KESTRIDGE PAINTING. ALL RIGHTS RESERVED.</div>
  <div class="follow">FOLLOW US :</div>
  <span class="social" style="left:577px"></span>
  <span class="social" style="left:604px"></span>
  <span class="social" style="left:631px"></span>
  <span class="social" style="left:658px"></span>
</footer>

</body>
</html>
```